Glen Holbrook Announces his new career move! 8x5 card please.

Associate Broker GLEN HOLBROOK is proud to announce his new affiliation with m.vorlund bayshore estates, ltd.

His goal remains to meet all your real estate needs. Prepare to renew your seasonal rental for 2016...with the full support of his new office, Glen can handle your renewal seamlessly.

Prepared to purchase? With access to every property on the market...Glen can show you how easy it making your summer dreams come true can be.

Thinking about selling? m.vorlund bayshore estates, ltd. now offers the benefits of the Multiple Listing Service (MLS) to all sellers. In cooperation with MLS Sellers receive the maximum worldwide exposure, Purchasers receive a larger volume of properties to view and in cooperation with other Realtors, the transaction is handled professionally!!!!

I will send logo and photo of Glen Holbrook separately. Thank you. P-
Updates

Target Market(s)

Tenants, Sellers & Buyers

Industry/Entity Type

Broker

Font styles to use
Sans Serif

Requirements
Must have
• I attached logo and photo of Glen. Added a better photo of Glen.
Nice to have
• A photo of a property we have listed. I added a couple to choose from.
Should not have
• No Red color

```html
<!DOCTYPE html>
<html lang="en">
<head>
<meta charset="utf-8">
<title>Glen Holbrook – New Affiliation Cards</title>
<link href="https://fonts.googleapis.com/css2?family=Open+Sans:wght@400;600&display=swap" rel="stylesheet">
<style>
  :root {
    --page-bg: #eeebe6;
    --card-bg: #ffffff;
    --cream: #faf7e4;
    --green-dark: #1f7a47;
    --green-band: #a5d08c;
    --green-pale: #cfe4c0;
    --text-gray: #555555;
    --name-gray: #444444;
    --sky: #8fbfe3;
    --villa-white: #e9ebe8;
    --pool: #5ccfd0;
    --sea: #5d93b5;
    --deck: #8a8279;
    --portrait-bg: #b8cbd6;
    --portrait-shirt: #3a3230;
  }
  * { margin: 0; padding: 0; box-sizing: border-box; }
  html, body { width: 1200px; height: 807px; overflow: hidden; }
  body {
    background: var(--page-bg);
    font-family: "Open Sans", Arial, sans-serif;
    position: relative;
  }
  .card {
    position: absolute;
    width: 503px;
    height: 694px;
    background: var(--card-bg);
    overflow: hidden;
    box-shadow: 0 1px 4px rgba(0,0,0,0.18);
  }
  .card--announce { left: 63px; top: 48px; }
  .card--services { left: 662px; top: 79px; }

  .cream-area { position: absolute; left: 0; right: 0; bottom: 0; background: var(--cream); }
  .card--announce .cream-area { top: 420px; }
  .card--services .cream-area { top: 440px; }

  .headline {
    position: absolute; left: 0; right: 0; top: 40px;
    text-align: center; color: var(--green-dark);
    font-size: 16.5px; line-height: 21px; font-weight: 400;
  }

  .photo { position: absolute; left: 0; width: 503px; }
  .photo--villa {
    top: 105px; height: 310px;
    background: linear-gradient(180deg, var(--sky) 0%, var(--villa-white) 45%, var(--villa-white) 62%, var(--pool) 100%);
  }
  .photo--beach {
    top: 0; height: 190px;
    background: linear-gradient(180deg, #c6dcee 0%, #e4ecf1 38%, var(--sea) 62%, var(--deck) 100%);
  }
  .wave { position: absolute; left: 0; width: 503px; display: block; }

  .thumbs { position: absolute; top: 406px; left: 203px; display: flex; gap: 7px; }
  .thumb { width: 86px; height: 85px; box-shadow: inset 0 0 0 1px rgba(0,0,0,0.06); }
  .thumb--deck { background: linear-gradient(180deg, #d3dde3 0%, #7d98a8 100%); }
  .thumb--kitchen { background: linear-gradient(180deg, #f1ede5 0%, #d6c7ac 100%); }
  .thumb--living { background: linear-gradient(180deg, #ecece6 0%, #b9c2bd 100%); }

  .portrait {
    position: absolute; left: 40px; top: 459px; width: 117px; height: 134px;
    background: linear-gradient(180deg, var(--portrait-bg) 0%, var(--portrait-bg) 40%, var(--portrait-shirt) 100%);
    box-shadow: inset 0 0 0 1px rgba(0,0,0,0.06);
  }
  .agent { position: absolute; left: 20px; width: 157px; top: 600px; text-align: center; }
  .agent__name { color: var(--name-gray); font-size: 13px; line-height: 17px; }
  .agent__phone {
    color: var(--green-dark); font-size: 13.5px; line-height: 18px; font-weight: 600;
    display: inline-flex; align-items: center; gap: 5px;
  }
  .agent__phone svg { width: 12px; height: 12px; }

  .body-copy {
    position: absolute; color: var(--text-gray);
    font-size: 11.6px; line-height: 15.5px; text-align: justify;
  }
  .card--announce .body-copy--goal { left: 203px; top: 510px; width: 270px; }
  .card--services .body-copy--goal { left: 202px; top: 476px; width: 272px; }

  .company-mark {
    position: absolute; display: flex; align-items: center; gap: 8px;
    color: var(--green-dark); font-size: 13px; font-weight: 600; white-space: nowrap;
  }
  .card--announce .company-mark { left: 216px; top: 600px; }
  .card--services .company-mark { left: 215px; top: 580px; }
  .company-mark__square { width: 12px; height: 12px; background: var(--green-dark); }

  .footer-band {
    position: absolute; left: 0; right: 0; height: 21px;
    background: var(--green-band); color: #fff;
    font-size: 11.5px; letter-spacing: 0.6px; text-align: center; line-height: 21px;
  }
  .card--announce .footer-band { top: 639px; }
  .card--services .footer-band { top: 640px; }

  .section-title {
    position: absolute; left: 24px; color: var(--green-dark);
    font-size: 15.5px; font-weight: 400; line-height: 20px;
  }
  .section-title--buy { top: 205px; }
  .section-title--sell { top: 284px; }
  .body-copy--buy { left: 24px; top: 229px; width: 460px; text-align: left; }
  .body-copy--sell { left: 24px; top: 313px; width: 455px; }
</style>
</head>
<body>

<article class="card card--announce">
  <div class="cream-area"></div>
  <h1 class="headline">Associate Broker GLEN HOLBROOK is proud to announce<br>his new affiliation with m.vorlund bayshore estates, ltd.</h1>

  <div class="photo photo--villa" role="img" aria-label="Photo of a modern white villa with a covered terrace and turquoise pool"></div>
  <svg class="wave" style="top:90px" width="503" height="45" viewBox="0 0 503 45">
    <path d="M0 0H503V22C420 2 300 28 170 24C100 22 40 18 0 30Z" fill="#fff"/>
    <path d="M0 30C40 18 100 22 170 24C300 28 420 2 503 22V30C420 12 300 38 170 34C100 32 40 28 0 40Z" fill="#a5d08c"/>
  </svg>
  <svg class="wave" style="top:380px" width="503" height="100" viewBox="0 0 503 100">
    <path d="M0 30C120 10 260 40 380 30C440 25 480 18 503 22V100H0Z" fill="#cfe4c0"/>
    <path d="M0 40C130 22 260 52 380 40C440 35 480 28 503 32V100H0Z" fill="#a5d08c"/>
    <path d="M0 58C120 38 250 62 370 50C430 44 480 40 503 44V100H0Z" fill="#cfe4c0"/>
    <path d="M0 78C100 60 220 48 320 44C400 42 470 40 503 42V100H0Z" fill="#faf7e4"/>
  </svg>

  <div class="thumbs">
    <div class="thumb thumb--deck" role="img" aria-label="Photo of a deck overlooking the bay"></div>
    <div class="thumb thumb--kitchen" role="img" aria-label="Photo of a bright kitchen interior"></div>
    <div class="thumb thumb--living" role="img" aria-label="Photo of a furnished living room"></div>
  </div>

  <div class="portrait" role="img" aria-label="Portrait photo of Glen Holbrook"></div>
  <div class="agent">
    <p class="agent__name">Glen Holbrook</p>
    <p class="agent__phone">
      <svg viewBox="0 0 24 24"><path fill="#1f7a47" d="M6.6 10.8a15.1 15.1 0 0 0 6.6 6.6l2.2-2.2a1 1 0 0 1 1-.25 11.4 11.4 0 0 0 3.6.57 1 1 0 0 1 1 1V20a1 1 0 0 1-1 1A17 17 0 0 1 3 4a1 1 0 0 1 1-1h3.5a1 1 0 0 1 1 1c0 1.250.2 2.450.57 3.57a1 1 0 0 1-.25 1z"/></svg>
      555.214.0386
    </p>
  </div>

  <p class="body-copy body-copy--goal">His goal remains to meet all your real estate needs. Prepare to renew your seasonal rental for 2016...with the full support of his new office, Glen can handle your renewal seamlessly.</p>

  <div class="company-mark"><span>m.vorlund bayshore estates, ltd.</span><span class="company-mark__square"></span></div>

  <div class="footer-band">www.bayshoreestates-demo.com</div>
</article>

<article class="card card--services">
  <div class="cream-area"></div>
  <div class="photo photo--beach" role="img" aria-label="Photo of an infinity pool terrace with loungers and umbrella facing the sea"></div>
  <svg class="wave" style="top:140px" width="503" height="60" viewBox="0 0 503 60">
    <path d="M0 40C120 20 260 34 380 20C440 13 480 10 503 12V60H0Z" fill="#cfe4c0"/>
    <path d="M0 50C130 30 260 44 380 30C440 23 480 22 503 24V60H0Z" fill="#fff"/>
  </svg>

  <h2 class="section-title section-title--buy">Prepared to purchase?</h2>
  <p class="body-copy body-copy--buy">With access to every property on the market...<br>Glen can show you how easy it making your summer dreams come true can be.</p>

  <h2 class="section-title section-title--sell">Thinking about selling?</h2>
  <p class="body-copy body-copy--sell">M.vorlund bayshore estates, ltd. now offers the benefits of the Multiple Listing Service (MLS) to all sellers.<br>In cooperation with MLS Sellers receive the maximum worldwide exposure, Purchasers receive a larger volume of properties to view and in cooperation with other Realtors, the transaction is handled professionally!!!!</p>

  <svg class="wave" style="top:420px" width="503" height="40" viewBox="0 0 503 40">
    <path d="M0 0H503V14C420 4 320 22 200 18C110 15 40 8 0 20Z" fill="#fff"/>
  </svg>

  <div class="portrait" role="img" aria-label="Portrait photo of Glen Holbrook"></div>
  <div class="agent">
    <p class="agent__name">Glen Holbrook</p>
    <p class="agent__phone">
      <svg viewBox="0 0 24 24"><path fill="#1f7a47" d="M6.6 10.8a15.1 15.1 0 0 0 6.6 6.6l2.2-2.2a1 1 0 0 1 1-.25 11.4 11.4 0 0 0 3.6.57 1 1 0 0 1 1 1V20a1 1 0 0 1-1 1A17 17 0 0 1 3 4a1 1 0 0 1 1-1h3.5a1 1 0 0 1 1 1c0 1.250.2 2.450.57 3.57a1 1 0 0 1-.25 1z"/></svg>
      555.214.0386
    </p>
  </div>

  <p class="body-copy body-copy--goal">His goal remains to meet all your real estate needs. Prepare to renew your seasonal rental for 2016...with the full support of his new office, Glen can handle your renewal seamlessly.</p>

  <div class="company-mark"><span>m.vorlund bayshore estates, ltd.</span><span class="company-mark__square"></span></div>

  <div class="footer-band">www.bayshoreestates-demo.com</div>
</article>

</body>
</html>
```